Property refurbishment & maintenance Business Card Design

Velmorin Ltd is a leading provider of domestic maintenance, building and refurbishment services. Founded in October 2009 by Piotr Velmorin, we aim to provide our customers with exceptional home improvement and maintenance services whilst minimising the disruption and stress caused.
The building services we provide are of the very highest quality. We provide all of your customers with the peace of mind in knowing that they are dealing with experts in construction, renovation and decoration. This is because we are members of the Guild of Craft Contractors (GCC). We have also had our credentials verified by Surelink and the UK government's Keel Seal scheme.
Target Market(s)
Private home owners,letting agents,tenants
Industry/Entity Type
Home Improvement
Contact Information for Business Card
Velmorin ltd.
Piotr Velmorin
14 Pellham Birch Lane ,Brackenmoor,Lorneshire,BM4 2QR,T.01707318257 M:07924168330
E. info@velmorin.example. www.velmorin.example
Look and feel
Each slider illustrates characteristics of the customer's brand and the style your logo design should communicate.

```html
<!DOCTYPE html>
<html lang="en">
<head>
<meta charset="utf-8">
<title>Velmorin Ltd – Business Card</title>
<link href="https://fonts.googleapis.com/css2?family=Lato:wght@400;700;900&display=swap" rel="stylesheet">
<style>
  :root {
    --bg: #2a2a2a;
    --card: #f4f4f4;
    --green: #1f5a4b;
    --ink: #1e1e1e;
    --white: #ffffff;
  }
  html, body {
    margin: 0;
    width: 1200px;
    height: 900px;
    overflow: hidden;
    background: var(--bg);
    font-family: "Lato", Arial, sans-serif;
  }
  .card {
    position: absolute;
    left: 100px;
    top: 165px;
    width: 1000px;
    height: 570px;
    background: var(--card);
    border-radius: 34px;
    overflow: hidden;
    box-shadow: 0 20px 50px rgba(0,0,0,.5);
  }
  .name-band {
    height: 86px;
    background: var(--green);
    display: flex;
    align-items: center;
    justify-content: flex-end;
    padding-right: 60px;
  }
  .person-name {
    color: var(--white);
    font-weight: 900;
    font-size: 30px;
    letter-spacing: .5px;
    text-transform: uppercase;
  }
  .brand {
    position: absolute;
    left: 70px;
    top: 150px;
  }
  .brand-name {
    display: flex;
    align-items: center;
    gap: 16px;
    color: var(--green);
    font-weight: 700;
    font-size: 60px;
    letter-spacing: 4px;
    text-transform: uppercase;
  }
  .brand-mark {
    width: 22px;
    height: 22px;
    background: var(--green);
  }
  .brand-web {
    margin-top: 6px;
    margin-left: 38px;
    color: var(--green);
    font-weight: 700;
    font-size: 22px;
    letter-spacing: 3px;
  }
  .services {
    position: absolute;
    right: 70px;
    top: 255px;
    text-align: right;
    color: var(--green);
    font-weight: 900;
    font-size: 24px;
    line-height: 1.2;
    text-transform: uppercase;
  }
  .contact {
    position: absolute;
    display: flex;
    align-items: center;
    gap: 12px;
    color: var(--ink);
    font-weight: 700;
    font-size: 25px;
    white-space: nowrap;
  }
  .contact svg { width: 26px; height: 26px; fill: var(--ink); flex: none; }
  .contact-address { left: 230px; top: 390px; }
  .contact-mobile { left: 70px; top: 470px; }
  .contact-phone { left: 390px; top: 470px; }
  .contact-email { right: 70px; top: 470px; }
</style>
</head>
<body>
  <div class="card">
    <header class="name-band">
      <span class="person-name">Piotr Velmorin</span>
    </header>

    <div class="brand">
      <div class="brand-name"><span class="brand-mark"></span>Velmorin</div>
      <div class="brand-web">www.velmorin.example</div>
    </div>

    <div class="services">Domestic maintenance, building<br>&amp; refurbishment services</div>

    <div class="contact contact-address">
      <svg viewBox="0 0 24 24"><path d="M12 3 1 12h3v9h6v-6h4v6h6v-9h3z"/></svg>
      14 Pellham Birch Lane ,Brackenmoor,Lorneshire,BM4 2QR
    </div>

    <div class="contact contact-mobile">
      <svg viewBox="0 0 24 24"><rect x="6" y="2" width="12" height="20" rx="2" fill="none" stroke="#1e1e1e" stroke-width="2"/><circle cx="12" cy="18" r="1"/></svg>
      07924168330
    </div>

    <div class="contact contact-phone">
      <svg viewBox="0 0 24 24"><path d="M6.6 10.8a15 15 0 0 0 6.6 6.6l2.2-2.2c.3-.3.7-.4 1-.2 1.1.4 2.3.6 3.6.6.6 0 1 .4 1 1V20c0 .6-.4 1-1 1A17 17 0 0 1 3 4c0-.6.4-1 1-1h3.5c.6 0 1 .4 1 1 0 1.3.2 2.5.6 3.6.1.3 0 .7-.2 1z"/></svg>
      +61402 718 605
    </div>

    <div class="contact contact-email">
      <svg viewBox="0 0 24 24"><path d="M2 5h20v14H2z M3.5 6.5 12 13l8.5-6.5" fill="none" stroke="#1e1e1e" stroke-width="2"/></svg>
      info@velmorin.example
    </div>
  </div>
</body>
</html>
```